Need a book cover design for a Lumora Book

Book has a long title and sub title so lots of words to fit on the cover.

I can be flexible a bit with the sub title due to the length of it but ideally i can get a design that takes everything.

Here is the title:

Tidal Geology: The Roots of Erosion, Sedimentation, and Canyon Forming

Sub Title/Heading
An Easy Primer on Coastal Cliffs, Dune Drift, River Beds, and Delta Mapping Methods

```html
<!DOCTYPE html>
<html lang="en">
<head>
<meta charset="utf-8">
<title>Tidal Geology – Book Cover</title>
<link rel="stylesheet" href="https://fonts.googleapis.com/css2?family=Anton&family=Fjalla+One&display=swap">
<style>
  :root {
    --ink: #252b36;
    --gold: #fcce74;
    --paper: #ffffff;
    --art-light: #f3f4f7;
    --art-mid: #e4e6ec;
  }
  html, body {
    margin: 0;
    padding: 0;
    overflow: hidden;
    background: var(--paper);
  }
  .cover {
    position: relative;
    width: 800px;
    height: 1200px;
    overflow: hidden;
    background: var(--paper);
  }
  .title-block {
    position: absolute;
    inset: 0 0 auto 0;
    width: 800px;
    height: 740px;
  }
  .title-display {
    font-family: "Anton", "Bebas Neue", sans-serif;
  }
  .title-feature { fill: var(--gold); }
  .title-shadow { fill: var(--ink); }
  .title-line { fill: var(--ink); }
  .subtitle {
    position: absolute;
    top: 748px;
    left: 0;
    width: 800px;
    margin: 0;
    text-align: center;
    font-family: "Fjalla One", "Oswald", sans-serif;
    font-size: 33px;
    line-height: 36px;
    color: #111111;
    letter-spacing: -0.3px;
  }
  .cover-art {
    position: absolute;
    top: 826px;
    left: 0;
    width: 800px;
    height: 296px;
    background: linear-gradient(180deg, var(--art-light) 0%, var(--art-mid) 100%);
  }
  .author-band {
    position: absolute;
    left: 0;
    bottom: 0;
    width: 800px;
    height: 78px;
    background: var(--ink);
    display: flex;
    align-items: center;
    justify-content: center;
  }
  .author-name {
    font-family: "Fjalla One", "Oswald", sans-serif;
    font-size: 50px;
    color: var(--gold);
    letter-spacing: 0.5px;
  }
</style>
</head>
<body>
<main class="cover">
  <svg class="title-block title-display" viewBox="0 0 800 740" role="heading" aria-level="1" aria-label="Tidal Geology: The Roots of Erosion, Sedimentation, and Canyon Forming">
    <g aria-hidden="true">
      <text class="title-shadow" x="107" y="206" font-size="212" textLength="590" lengthAdjust="spacingAndGlyphs">TIDAL</text>
      <text class="title-feature" x="101" y="200" font-size="212" textLength="590" lengthAdjust="spacingAndGlyphs">TIDAL</text>

      <text class="title-line" x="400" y="318" font-size="96" text-anchor="middle" textLength="520" lengthAdjust="spacingAndGlyphs">THE ROOTS OF EROSION,</text>
      <text class="title-line" x="400" y="416" font-size="96" text-anchor="middle" textLength="440" lengthAdjust="spacingAndGlyphs">SEDIMENTATION,</text>
      <text class="title-line" x="400" y="514" font-size="96" text-anchor="middle" textLength="530" lengthAdjust="spacingAndGlyphs">AND CANYON FORMING</text>

      <text class="title-shadow" x="128" y="733" font-size="212" textLength="560" lengthAdjust="spacingAndGlyphs">GEOLOGY</text>
      <text class="title-feature" x="122" y="727" font-size="212" textLength="560" lengthAdjust="spacingAndGlyphs">GEOLOGY</text>
    </g>
  </svg>

  <p class="subtitle">An Easy Primer on Coastal Cliffs, Dune Drift,<br>River Beds, and Delta Mapping Methods</p>

  <div class="cover-art" role="img" aria-label="Line-drawn doodle illustration of a scientist surrounded by geology and science sketches, formulas and small icons"></div>

  <footer class="author-band">
    <span class="author-name">Author Name</span>
  </footer>
</main>
</body>
</html>
```